I need an out door banner to help me promote my classes, i am a dating coach. i would like to see designs that use the colors. black, yellow, pink, white,orange. colors that attract women. the final design should communicate how women can Reclaim Every Spark, Shine Once More.

Target Market(s)

Bright Mornings After Midnight Storms: Reclaim Every Spark, Shine Once More: Heartfelt Wisdom on Modern Courtship

Industry/Entity Type

dating advice

Logo Text

Attention Ladies: Weed out the Narcissist, the abusers, the couch potatoes, the players & the losers...( Expose & Dump his #ss before he destroys your life)

Colors

Designer to choose colors to be used in the design.

Requirements
Nice to have
• Some bold text too
Should not have
• black round

```html
<!DOCTYPE html>
<html lang="en">
<head>
<meta charset="utf-8">
<title>Attention Ladies – Dating Coach Banner</title>
<link rel="stylesheet" href="https://fonts.googleapis.com/css2?family=Montserrat:wght@800&display=swap">
<style>
  :root {
    --page-bg: #ffffff;
    --banner-pink: #d91c5c;
    --banner-text: #ffffff;
  }
  html, body {
    margin: 0;
    padding: 0;
    width: 1200px;
    height: 900px;
    overflow: hidden;
    background: var(--page-bg);
  }
  .canvas {
    position: relative;
    width: 1200px;
    height: 900px;
  }
  .banner {
    position: absolute;
    left: 379px;
    top: 229px;
    width: 442px;
    height: 441px;
  }
  .banner-bg { fill: var(--banner-pink); }
  .banner-line {
    fill: var(--banner-text);
    font-family: "Montserrat", sans-serif;
    font-weight: 800;
    letter-spacing: -0.5px;
  }
</style>
</head>
<body>
  <main class="canvas">
    <svg class="banner" viewBox="0 0 442 441" role="group" aria-label="Attention Ladies banner">
      <rect class="banner-bg" x="0" y="0" width="442" height="441"/>
      <text class="banner-line headline" x="20" y="56" font-size="40" textLength="402" lengthAdjust="spacingAndGlyphs">Attention Ladies:</text>
      <text class="banner-line" x="20" y="97" font-size="30" textLength="402" lengthAdjust="spacingAndGlyphs">Weed out the Narcissist</text>
      <text class="banner-line emphasis" x="20" y="159" font-size="62" textLength="402" lengthAdjust="spacingAndGlyphs">the abusers</text>
      <text class="banner-line" x="20" y="205" font-size="36" textLength="402" lengthAdjust="spacingAndGlyphs">the couch potatoes</text>
      <text class="banner-line emphasis" x="20" y="269" font-size="62" textLength="402" lengthAdjust="spacingAndGlyphs">the players</text>
      <text class="banner-line emphasis" x="20" y="331" font-size="54" textLength="402" lengthAdjust="spacingAndGlyphs">&amp; the losers...</text>
      <text class="banner-line" x="20" y="374" font-size="34" textLength="402" lengthAdjust="spacingAndGlyphs">Expose &amp; Dump his #ss</text>
      <text class="banner-line" x="20" y="414" font-size="26" textLength="402" lengthAdjust="spacingAndGlyphs">before he destroys your life</text>
    </svg>
  </main>
</body>
</html>
```